Hollow Covenant book cover.

Book cover design. Files must be in an accepted format by QWL Press for publishing.
Final book cover will need to be adjusted after acceptance. The spline anyway. Not the overall design.
Placement of bar code on back after design is done.
I can’t get the ISBN number until the cover is finalized.

Book blurb text on back
Title of the book is “Hollow Covenant.”

Book Blurb on back of cover below
Hollow covenant.
A fictional novel based on current events surrounding the covid 19 virous. Owen Pratley is a well-respected independent journalist contracted by the Harbor Ridge Ledger, upon his return from reporting on the war in Syria he is tasked to investigate the covid virus outbreak in China. As he digs deeper, he uncovers a hideous plot by the powers that be here in America. Owen risks life and limb to uncover the conspirators behind all of this and shed light to the American people.

```html
<!DOCTYPE html>
<html lang="en">
<head>
<meta charset="utf-8">
<title>Hollow Covenant – Cover Spread</title>
<link href="https://fonts.googleapis.com/css2?family=Oranienbaum&family=EB+Garamond:wght@400&family=Bodoni+Moda:wght@400;500&display=swap" rel="stylesheet">
<style>
  :root {
    --page-bg: #ececec;
    --cover-black: #0c0c0c;
    --back-black: #111111;
    --spine-black: #0a0a0a;
    --ink-white: #f4f4f4;
    --title-silver: #e6e6e6;
    --title-shadow: rgba(0,0,0,0.85);
    --flag-blue: #1f2a6b;
    --flag-red: #8d1a1c;
    --dome-grey: #2a2a2a;
  }
  * { margin: 0; padding: 0; box-sizing: border-box; }
  html, body {
    width: 899px; height: 1200px; overflow: hidden;
    background: var(--page-bg);
  }
  .canvas {
    position: relative; width: 899px; height: 1200px;
    display: flex; align-items: center; justify-content: center;
  }
  .spread {
    position: relative; width: 880px; height: 610px;
    display: flex; box-shadow: 0 10px 30px rgba(0,0,0,0.25);
  }

  /* Back cover */
  .back-cover {
    position: relative; width: 434px; height: 100%;
    background: var(--back-black); overflow: hidden;
  }
  .back-cover .capitol-art {
    position: absolute; left: 0; bottom: 0; width: 300px; height: 430px;
    background: radial-gradient(ellipse at 25% 55%, #3a3a3a 0%, var(--dome-grey) 35%, rgba(17,17,17,0) 75%);
    opacity: 0.8;
  }
  .back-title {
    position: absolute; top: 70px; left: 0; width: 434px; text-align: center;
    font-family: "Oranienbaum", serif; color: var(--title-silver);
    text-shadow: 2px 3px 3px var(--title-shadow);
  }
  .back-title .line-top { font-size: 30px; letter-spacing: 0.5px; line-height: 1; }
  .back-title .line-main { font-size: 50px; line-height: 1.05; }
  .blurb {
    position: absolute; top: 200px; left: 51px; width: 328px;
    font-family: "EB Garamond", serif; font-size: 14.2px; line-height: 17.8px;
    color: var(--ink-white); text-align: justify;
  }
  .barcode-space {
    position: absolute; left: 273px; top: 509px; width: 92px; height: 53px;
    background: #ffffff;
  }

  /* Spine */
  .spine {
    position: relative; width: 48px; height: 100%;
    background: var(--spine-black);
  }
  .spine-star { position: absolute; left: 13px; width: 22px; height: 22px; fill: var(--ink-white); }
  .spine-star.top { top: 28px; }
  .spine-star.bottom { top: 380px; }
  .spine-title {
    position: absolute; left: 24px; top: 215px;
    transform: translate(-50%, -50%) rotate(-90deg);
    white-space: nowrap;
    font-family: "Bodoni Moda", serif; font-size: 22px; letter-spacing: 0.5px;
    color: var(--ink-white);
  }
  .spine-author {
    position: absolute; left: 24px; top: 512px;
    transform: translate(-50%, -50%) rotate(-90deg);
    white-space: nowrap;
    font-family: "Bodoni Moda", serif; font-size: 9px; letter-spacing: 4px;
    color: var(--ink-white);
  }

  /* Front cover */
  .front-cover {
    position: relative; width: 398px; height: 100%;
    background: var(--cover-black); overflow: hidden;
  }
  .front-cover .hero-art {
    position: absolute; inset: 0;
    background:
      radial-gradient(ellipse at 75% 40%, rgba(120,120,120,0.55) 0%, rgba(40,40,40,0.4) 35%, rgba(12,12,12,0) 65%),
      linear-gradient(180deg, var(--flag-blue) 0%, #2a2f5a 18%, var(--flag-red) 38%, #3a1414 58%, var(--cover-black) 78%);
    -webkit-mask-image: linear-gradient(90deg, #000 0%, #000 60%, #000 100%);
  }
  .front-cover .hero-fade {
    position: absolute; inset: 0;
    background: linear-gradient(90deg, rgba(12,12,12,0) 0%, rgba(12,12,12,0) 30%, rgba(12,12,12,0.25) 100%);
  }
  .author-name {
    position: absolute; top: 20px; left: 0; width: 398px; text-align: center;
    font-family: "Bodoni Moda", serif; font-size: 22px; letter-spacing: 9px;
    color: var(--ink-white);
    text-shadow: 1px 2px 3px var(--title-shadow);
  }
  .front-title {
    position: absolute; top: 395px; left: 0; width: 398px; text-align: center;
    font-family: "Oranienbaum", serif; color: var(--title-silver);
    text-shadow: 3px 4px 4px var(--title-shadow);
  }
  .front-title .line-top { font-size: 52px; line-height: 1; }
  .front-title .line-main { font-size: 82px; line-height: 1.05; }
  .star-inline { display: inline-block; width: 0.45em; height: 0.45em; vertical-align: 0.15em; fill: var(--title-silver); margin: 0 0.2em; }
</style>
</head>
<body>
<div class="canvas">
  <div class="spread">

    <section class="back-cover">
      <div class="capitol-art" role="img" aria-label="Faint night view of the Capitol dome with a flag"></div>
      <h2 class="back-title">
        <div class="line-top"><svg class="star-inline" viewBox="0 0 24 24"><polygon points="12,1 15,9 23,9 16.5,14 19,22 12,17 5,22 7.5,14 1,9 9,9"/></svg>HOLLOW<svg class="star-inline" viewBox="0 0 24 24"><polygon points="12,1 15,9 23,9 16.5,14 19,22 12,17 5,22 7.5,14 1,9 9,9"/></svg></div>
        <div class="line-main">COVENANT</div>
      </h2>
      <p class="blurb">A fictional novel based on current events surrounding the covid 19 virous. Owen Pratley is a well-respected independent journalist contracted by the Harbor Ridge Ledger, upon his return from reporting on the war in Syria he is tasked to investigate the covid virus outbreak in China. As he digs deeper, he uncovers a hideous plot by the powers that be here in America. Owen risks life and limb to uncover the conspirators behind all of this and shed light to the American people.</p>
      <div class="barcode-space"></div>
    </section>

    <section class="spine">
      <svg class="spine-star top" viewBox="0 0 24 24"><polygon points="12,1 15,9 23,9 16.5,14 19,22 12,17 5,22 7.5,14 1,9 9,9"/></svg>
      <div class="spine-title">HOLLOW COVENANT</div>
      <svg class="spine-star bottom" viewBox="0 0 24 24"><polygon points="12,1 15,9 23,9 16.5,14 19,22 12,17 5,22 7.5,14 1,9 9,9"/></svg>
      <div class="spine-author">AUTHOR NAME</div>
    </section>

    <section class="front-cover">
      <div class="hero-art" role="img" aria-label="Profile portrait of a man in dark suit over a blended flag and Capitol building backdrop"></div>
      <div class="hero-fade"></div>
      <div class="author-name">AUTHOR NAME</div>
      <h1 class="front-title">
        <div class="line-top"><svg class="star-inline" viewBox="0 0 24 24"><polygon points="12,1 15,9 23,9 16.5,14 19,22 12,17 5,22 7.5,14 1,9 9,9"/></svg>HOLLOW<svg class="star-inline" viewBox="0 0 24 24"><polygon points="12,1 15,9 23,9 16.5,14 19,22 12,17 5,22 7.5,14 1,9 9,9"/></svg></div>
        <div class="line-main">COVENANT</div>
      </h1>
    </section>

  </div>
</div>
</body>
</html>
```